" A Vendaluz Store comercializa produtos nos seguintes segmentos: automotivo, cine e foto, componentes, cuidados pessoais, eletrodomésticos e eletroportáteis, eletrônicos, games, informatica, instrumentos musicais, materiais elétricos, som profissional e telefonia além de produtos de decoração. Tem como objetivo fornecer produtos de excelência e proporcionar uma marcante experiência de compra na modalidade e-commerce. "

```html
<!DOCTYPE html>
<html lang="pt-BR">
<head>
<meta charset="UTF-8">
<title>Vendaluz Store – Cartão de Visita</title>
<link href="https://fonts.googleapis.com/css2?family=Montserrat:ital,wght@0,300;0,400;0,700;1,400&display=swap" rel="stylesheet">
<style>
  :root {
    --bg: #d9dadc;
    --card: #0f1d22;
    --card-deep: #0a1418;
    --gold: #d9a93a;
    --gold-light: #f3d27a;
    --gold-dark: #a8771c;
    --white: #ffffff;
    --muted: #c9cfd2;
  }
  * { margin: 0; padding: 0; box-sizing: border-box; }
  html, body {
    width: 1200px; height: 1200px; overflow: hidden;
    background: var(--bg);
    font-family: "Montserrat", sans-serif;
  }
  .sheet {
    width: 1200px; height: 1200px;
    display: flex; flex-direction: column;
    align-items: center; justify-content: center; gap: 60px;
  }
  .card {
    position: relative;
    width: 960px; height: 533px;
    border-radius: 26px;
    background: linear-gradient(135deg, var(--card) 0%, var(--card-deep) 100%);
    overflow: hidden;
    box-shadow: 0 18px 40px rgba(0,0,0,.25);
  }
  .gold-fill { background: linear-gradient(90deg, var(--gold-dark), var(--gold-light) 45%, var(--gold) 70%, var(--gold-dark)); }

  /* front */
  .front__rule {
    position: absolute; left: 0; right: 0; bottom: 70px; height: 4px;
  }
  .front__edge {
    position: absolute; right: 0; top: 0; bottom: 0; width: 14px;
  }
  .brand {
    position: absolute; left: 50%; top: 50%;
    transform: translate(-50%, -50%);
    display: flex; align-items: center; gap: 26px;
  }
  .brand__mark {
    width: 34px; height: 34px;
  }
  .brand__name {
    color: var(--white);
    font-weight: 300;
    font-size: 52px;
    letter-spacing: 10px;
    text-transform: uppercase;
    white-space: nowrap;
  }

  /* back */
  .back__corner {
    position: absolute; left: 0; top: 0; width: 300px; height: 533px;
  }
  .back__rule {
    position: absolute; left: 0; right: 0; bottom: 58px; height: 4px;
  }
  .back__square {
    position: absolute; left: 90px; top: 150px; width: 90px; height: 90px;
  }
  .person {
    position: absolute; right: 70px; top: 70px; text-align: right;
  }
  .person__name {
    color: var(--white); font-weight: 700; font-size: 40px; letter-spacing: 2px;
  }
  .person__role {
    color: var(--white); font-weight: 400; font-style: italic; font-size: 24px; margin-top: 4px;
  }
  .contact {
    position: absolute; right: 70px; top: 200px;
    list-style: none; display: flex; flex-direction: column; gap: 18px;
  }
  .contact__item {
    display: flex; align-items: center; justify-content: flex-end; gap: 18px;
    color: var(--muted); font-size: 20px; line-height: 1.3; text-align: right;
  }
  .contact__icon {
    flex: none; width: 34px; height: 34px;
  }
</style>
</head>
<body>
<main class="sheet">

  <section class="card card--front" aria-label="Frente do cartão">
    <div class="brand">
      <span class="brand__mark gold-fill" aria-hidden="true"></span>
      <span class="brand__name">Vendaluz Store</span>
    </div>
    <div class="front__rule gold-fill"></div>
    <div class="front__edge gold-fill"></div>
  </section>

  <section class="card card--back" aria-label="Verso do cartão">
    <svg class="back__corner" viewBox="0 0 300 533" aria-hidden="true">
      <defs>
        <linearGradient id="goldGrad" x1="0" y1="0" x2="1" y2="1">
          <stop offset="0" stop-color="#f3d27a"/>
          <stop offset=".5" stop-color="#d9a93a"/>
          <stop offset="1" stop-color="#a8771c"/>
        </linearGradient>
      </defs>
      <polygon points="0,0 300,0 0,420" fill="url(#goldGrad)"/>
    </svg>

    <div class="person">
      <div class="person__name">NOME COMPLETO</div>
      <div class="person__role">Cargo</div>
    </div>

    <ul class="contact">
      <li class="contact__item">
        <span>(00) 0000000<br>(00) 0000000</span>
        <svg class="contact__icon" viewBox="0 0 34 34" aria-hidden="true">
          <circle cx="17" cy="17" r="16" fill="none" stroke="#d9a93a" stroke-width="2"/>
          <path d="M12 10c1-1 2-1 3 0l1.5 2.5c.5 1 0 2-.8 2.5 1 2 2.3 3.3 4.3 4.3.5-.8 1.5-1.3 2.5-.8L25 20c1 1 1 2 0 3-3 3-15-9-13-13z" fill="#d9a93a"/>
        </svg>
      </li>
      <li class="contact__item">
        <span>Rua das Acácias Douradas, 21<br>Sala 02 – Jardim Aurora |<br>São Paulo – S.P. – Unidade I</span>
        <svg class="contact__icon" viewBox="0 0 34 34" aria-hidden="true">
          <circle cx="17" cy="17" r="16" fill="none" stroke="#d9a93a" stroke-width="2"/>
          <path d="M17 8a6 6 0 0 0-6 6c0 5 6 12 6 12s6-7 6-12a6 6 0 0 0-6-6zm0 8.5a2.5 2.5 0 1 1 0-5 2.5 2.5 0 0 1 0 5z" fill="#d9a93a"/>
        </svg>
      </li>
      <li class="contact__item">
        <span>www.vendaluzstore.com</span>
        <svg class="contact__icon" viewBox="0 0 34 34" aria-hidden="true">
          <circle cx="17" cy="17" r="16" fill="none" stroke="#d9a93a" stroke-width="2"/>
          <circle cx="17" cy="17" r="8" fill="none" stroke="#d9a93a" stroke-width="1.8"/>
          <ellipse cx="17" cy="17" rx="3.5" ry="8" fill="none" stroke="#d9a93a" stroke-width="1.5"/>
          <line x1="9" y1="17" x2="25" y2="17" stroke="#d9a93a" stroke-width="1.5"/>
        </svg>
      </li>
    </ul>

    <div class="back__rule gold-fill"></div>
  </section>

</main>
</body>
</html>
```